Pellham Ridge Nectar Company, local Honey producer needs product Lable to encourage sales

We are a small business (Pellham Ridge Nectar Company) located in a small Valley town that harvests honey from our beehives yearly. Our honey would be considered "raw wildflower honey" and our goal is to sell it locally (farmers markets) and to surrounding areas.

We are currently packaging in plastic classic honey bottles with white flip caps. Sizes are 8oz and 16oz bottles (see pictures for actual size). Larger orders will be filled in one quart mason jars.

Design Ideas:
-vintage style design with bee or several bees in background
- incorporate company name "Pellham Ridge Nectar Company"
- needs small description "Raw Honey", and "Harvested in Bramwick, Valley"

Target Market(s)

Farmers markets, health conscience people looking for unprocessed food options

Industry/Entity Type

Small Business

Requirements
Nice to have
• Vintage feel
Should not have
• No cartoonish characters

```html
<!DOCTYPE html>
<html lang="en">
<head>
<meta charset="utf-8">
<title>Pellham Ridge Nectar Company – Raw Honey Labels</title>
<link rel="stylesheet" href="https://fonts.googleapis.com/css2?family=Federo&family=Cinzel:wght@700&display=swap">
<style>
  :root {
    --page: #ffffff;
    --ink: #3b2a22;
    --rule: #6d6a2c;
    --frame: #d9bccf;
    --frame-dark: #9b7f95;
    --copper-top: #b45a3d;
    --copper-mid: #f2bd9c;
    --copper-low: #8e4527;
    --copper-rim: #cf6e5e;
    --gold-top: #6b4517;
    --gold-mid: #ecd196;
    --gold-low: #6a3f12;
    --gold-rim: #d7a45a;
    --bee-dark: #6b3e12;
    --bee-light: #d59a3a;
  }
  html, body {
    margin: 0;
    padding: 0;
    width: 848px;
    height: 1200px;
    overflow: hidden;
    background: var(--page);
  }
  .canvas {
    position: relative;
    width: 848px;
    height: 1200px;
  }
  .label {
    position: absolute;
    top: 62px;
    width: 272px;
    height: 416px;
  }
  .label--copper { left: 108px; }
  .label--gold { left: 450px; }
  .label__tagline {
    font-family: "Federo", sans-serif;
    font-size: 15px;
    letter-spacing: 2.5px;
    fill: var(--ink);
  }
  .label__name {
    font-family: "Federo", sans-serif;
    font-size: 19.5px;
    letter-spacing: 1.2px;
    fill: var(--ink);
  }
  .label__origin {
    font-family: "Federo", sans-serif;
    font-size: 10.5px;
    letter-spacing: 1.8px;
    fill: var(--ink);
  }
  .label__region {
    font-family: "Cinzel", serif;
    font-weight: 700;
    font-size: 10.5px;
    letter-spacing: 3px;
    fill: var(--ink);
  }
  .label__rule {
    stroke: var(--rule);
    stroke-width: 2.5;
    stroke-linecap: round;
  }
  .label__frame {
    fill: none;
    stroke: var(--frame);
    stroke-width: 5;
  }
  .label__frame-edge {
    fill: none;
    stroke: var(--frame-dark);
    stroke-width: 1;
  }
</style>
</head>
<body>
<main class="canvas">

  <svg class="label label--copper" viewBox="0 0 272 416" xmlns="http://www.w3.org/2000/svg">
    <defs>
      <linearGradient id="copper-fill" x1="0" y1="0" x2="0" y2="1">
        <stop offset="0" stop-color="var(--copper-top)"/>
        <stop offset="0.2" stop-color="var(--copper-top)"/>
        <stop offset="0.42" stop-color="var(--copper-mid)"/>
        <stop offset="0.58" stop-color="#c27856"/>
        <stop offset="1" stop-color="var(--copper-low)"/>
      </linearGradient>
      <linearGradient id="bee-tone-a" x1="0" y1="0" x2="1" y2="0">
        <stop offset="0" stop-color="var(--bee-dark)"/>
        <stop offset="1" stop-color="var(--bee-light)"/>
      </linearGradient>
    </defs>
    <rect x="2" y="2" width="268" height="412" rx="134" fill="url(#copper-fill)" stroke="var(--copper-rim)" stroke-width="4"/>
    <rect class="label__bee" x="62" y="36" width="120" height="50" rx="22" fill="url(#bee-tone-a)" role="img" aria-label="Illustration of a honey bee perched on the hexagon frame"/>
    <polygon class="label__frame" points="136,83 254,150 254,288 136,358 20,288 20,150"/>
    <polygon class="label__frame-edge" points="136,89 249,153 249,285 136,352 25,285 25,153"/>
    <text class="label__tagline" x="136" y="155" text-anchor="middle">RAW HONEY</text>
    <line class="label__rule" x1="57" y1="170" x2="104" y2="170"/>
    <line class="label__rule" x1="160" y1="170" x2="208" y2="170"/>
    <text class="label__name" x="136" y="214" text-anchor="middle">PELLHAM RIDGE</text>
    <text class="label__name" x="136" y="240" text-anchor="middle">NECTAR COMPANY</text>
    <text class="label__origin" x="136" y="275" text-anchor="middle">HARVESTED IN BRAMWICK</text>
    <line class="label__rule" x1="57" y1="289" x2="104" y2="289"/>
    <line class="label__rule" x1="160" y1="289" x2="208" y2="289"/>
    <text class="label__region" x="136" y="315" text-anchor="middle">VALLEY</text>
  </svg>

  <svg class="label label--gold" viewBox="0 0 272 416" xmlns="http://www.w3.org/2000/svg">
    <defs>
      <linearGradient id="gold-fill" x1="0" y1="0" x2="0" y2="1">
        <stop offset="0" stop-color="var(--gold-top)"/>
        <stop offset="0.18" stop-color="#a77a36"/>
        <stop offset="0.4" stop-color="var(--gold-mid)"/>
        <stop offset="0.6" stop-color="#b08444"/>
        <stop offset="1" stop-color="var(--gold-low)"/>
      </linearGradient>
      <linearGradient id="bee-tone-b" x1="0" y1="0" x2="1" y2="0">
        <stop offset="0" stop-color="var(--bee-dark)"/>
        <stop offset="1" stop-color="var(--bee-light)"/>
      </linearGradient>
    </defs>
    <rect x="2" y="2" width="268" height="412" rx="134" fill="url(#gold-fill)" stroke="var(--gold-rim)" stroke-width="4"/>
    <rect class="label__bee" x="62" y="36" width="120" height="50" rx="22" fill="url(#bee-tone-b)" role="img" aria-label="Illustration of a honey bee perched on the hexagon frame"/>
    <polygon class="label__frame" points="136,83 254,150 254,288 136,358 20,288 20,150"/>
    <polygon class="label__frame-edge" points="136,89 249,153 249,285 136,352 25,285 25,153"/>
    <text class="label__tagline" x="136" y="155" text-anchor="middle">RAW HONEY</text>
    <line class="label__rule" x1="57" y1="170" x2="104" y2="170"/>
    <line class="label__rule" x1="160" y1="170" x2="208" y2="170"/>
    <text class="label__name" x="136" y="214" text-anchor="middle">PELLHAM RIDGE</text>
    <text class="label__name" x="136" y="240" text-anchor="middle">NECTAR COMPANY</text>
    <text class="label__origin" x="136" y="275" text-anchor="middle">HARVESTED IN BRAMWICK</text>
    <line class="label__rule" x1="57" y1="289" x2="104" y2="289"/>
    <line class="label__rule" x1="160" y1="289" x2="208" y2="289"/>
    <text class="label__region" x="136" y="315" text-anchor="middle">VALLEY</text>
  </svg>

</main>
</body>
</html>
```